Modern Banner and Window Decal Design For Law Firm Lawyer

We are looking for three modern and sophisticated banner design and window decal for our law firm.

Banner measurements/types:

1) Height: 130 cm Width: 160 cm (Outdoor banner)
2) Height: 200 cm Width: 85 cm (Pull up/retractable indoor banner)

Window Decal:
3) Height: 70cm width 70cm

Our law firm is based in Melbourne, Australia and we deal with property law mostly.

We prefer a white background with classic text in black or grey. We would also like a dash of colour so please use a green, blue or aqua colour palette that is consistent with our logo. Vector attached. A nice photo of property, Melbourne city viee, or family home would be nice.

We do not want any law related images - scales of justice, gavel or the like.

Our ultimate goal is to communicate that the firm is modern, professional and knowledgeable

We would like the following:

1. Our logo
2. Our services: - Property Law - Wills - Powers of Attorney - Probate - Estate Administration - Consultancy & Agency
3. Phone number
4. Web Address

5. For pull up/retractable banner we would also like the following text:

We use the latest digital technology and fixed-fees to provide fast and affordable legal advice that is easy to understand.

For privacy reasons, we will provide business details once we have decided on the winner.

We will monitor entries closely and promise to provide feedback and guidance on each entry.

Thank you very much for considering this project.

Target Market(s)

General public, professionals, lawyers and conveyancers

Industry/Entity Type

Law Firm

Font styles to use
Sans Serif

Colors
0393ce
34a6d7
0456a4
3176b5
acd037
33b8a4
86cfc6
00a990
9ccb3b

Requirements
Must have
• 1. Our logo
• 2. Our services: - Property Law - Wills - Powers of Attorney - Probate & Estate Administration - Consultancy & Agency
• 3. Phone number
• 4. Web Address
Nice to have
• Picture of Melbourne, Australia city ; property/buildings/lawyers
Should not have
• We do not want any law related images - scales of justice, gavel or the like.

```html
<!DOCTYPE html>
<html lang="en">
<head>
<meta charset="utf-8">
<title>Ridgeview Lawyers – Pull-up Banner</title>
<link href="https://fonts.googleapis.com/css2?family=Raleway:wght@300;400;500&display=swap" rel="stylesheet">
<style>
  :root {
    --stage: #9a9a9a;
    --paper: #ffffff;
    --paper-low: #dfe1e3;
    --ink: #4a4d52;
    --ink-soft: #3f4a55;
    --teal: #33b8a4;
    --teal-deep: #2d9aa8;
    --aqua: #34a6d7;
    --sky: #86c4ea;
    --sky-pale: #c6e6f7;
    --green: #9ccb3b;
    --lime: #acd037;
    --white: #ffffff;
  }
  * { box-sizing: border-box; margin: 0; padding: 0; }
  html, body { width: 902px; height: 1200px; overflow: hidden; }
  body { background: var(--stage); font-family: "Raleway", sans-serif; position: relative; }

  .banner {
    position: absolute; left: 209px; top: 0;
    width: 484px; height: 1200px; overflow: hidden;
    background: linear-gradient(180deg, var(--paper) 0%, var(--paper) 62%, var(--paper-low) 96%);
  }
  .banner__art { position: absolute; left: 0; top: 0; }

  .brand { position: absolute; left: 60px; top: 58px; display: flex; align-items: center; gap: 18px; }
  .brand__mark { width: 90px; height: 90px; border-radius: 50%; background: var(--aqua); flex: none; }
  .brand__name { color: var(--ink); font-weight: 500; line-height: 1.05; letter-spacing: 1px; }
  .brand__name-top { display: block; font-size: 38px; }
  .brand__name-bottom { display: block; font-size: 27px; letter-spacing: 2px; }

  .services {
    position: absolute; right: 16px; top: 218px; list-style: none; text-align: right;
    color: var(--ink-soft); font-weight: 300; font-size: 22px; line-height: 29.5px;
  }

  .features { position: absolute; left: 24px; top: 893px; width: 450px; }
  .feature { position: absolute; left: 0; display: flex; gap: 17px; }
  .feature:nth-child(1) { top: 0; }
  .feature:nth-child(2) { top: 90px; }
  .feature:nth-child(3) { top: 173px; }
  .feature__icon {
    width: 55px; height: 58px; border-radius: 5px; background: var(--teal-deep);
    flex: none; display: flex; align-items: center; justify-content: center;
  }
  .feature__text { color: var(--ink); font-size: 15px; font-weight: 400; line-height: 21px; padding-top: 2px; width: 375px; }

  .contact-bar {
    position: absolute; left: 0; bottom: 0; width: 484px; height: 42px;
    background: var(--lime); color: var(--white);
    display: flex; align-items: center; font-size: 20px; font-weight: 400;
  }
  .contact-bar__item { display: flex; align-items: center; gap: 6px; position: absolute; }
  .contact-bar__item--phone { left: 36px; }
  .contact-bar__item--web { left: 193px; }
</style>
</head>
<body>
<main class="banner">
  <svg class="banner__art" width="484" height="1200" viewBox="0 0 484 1200">
    <defs>
      <linearGradient id="paleArc" x1="0" y1="0" x2="1" y2="1">
        <stop offset="0" stop-color="#d9f0fb"/>
        <stop offset="1" stop-color="#a9daf3"/>
      </linearGradient>
      <linearGradient id="sceneFill" x1="0" y1="0" x2="0" y2="1">
        <stop offset="0" stop-color="#7fb9e6"/>
        <stop offset="0.45" stop-color="#9fcdee"/>
        <stop offset="0.6" stop-color="#7c95ad"/>
        <stop offset="0.75" stop-color="#6fa346"/>
        <stop offset="0.9" stop-color="#c9c4ba"/>
        <stop offset="1" stop-color="#5d9a36"/>
      </linearGradient>
    </defs>
    <circle cx="500" cy="560" r="440" fill="url(#paleArc)"/>
    <circle cx="455" cy="520" r="352" fill="var(--green)"/>
    <circle cx="466" cy="512" r="340" fill="var(--teal)"/>
    <circle cx="478" cy="512" r="326" fill="url(#sceneFill)" role="img"
            aria-label="Photo of the Melbourne city skyline above parkland, with a large family home in the foreground"/>
  </svg>

  <div class="brand">
    <span class="brand__mark"></span>
    <span class="brand__name">
      <span class="brand__name-top">RIDGEVIEW</span>
      <span class="brand__name-bottom">LAWYERS</span>
    </span>
  </div>

  <ul class="services">
    <li>Property Law</li>
    <li>Wills</li>
    <li>Powers of Attorney</li>
    <li>Consultancy &amp; Agency</li>
    <li>Probate &amp; Estate Administration</li>
  </ul>

  <section class="features">
    <div class="feature">
      <span class="feature__icon">
        <svg width="30" height="40" viewBox="0 0 30 40" fill="none" stroke="#fff" stroke-width="2.5">
          <rect x="4" y="2" width="20" height="34" rx="3"/>
          <circle cx="14" cy="18" r="5"/>
        </svg>
      </span>
      <p class="feature__text">We use the latest digital technology and fixed-fees to provide fast and affordable legal advice that is easy to understand.</p>
    </div>
    <div class="feature">
      <span class="feature__icon">
        <svg width="36" height="36" viewBox="0 0 36 36" fill="#fff">
          <circle cx="8" cy="9" r="4"/><rect x="4" y="15" width="8" height="16" rx="2"/>
          <circle cx="18" cy="8" r="4.5"/><rect x="13.5" y="14" width="9" height="18" rx="2"/>
          <circle cx="28" cy="9" r="4"/><rect x="24" y="15" width="8" height="16" rx="2"/>
        </svg>
      </span>
      <p class="feature__text">For privacy reasons, we will provide business details once we have decided on the winner.</p>
    </div>
    <div class="feature">
      <span class="feature__icon">
        <svg width="38" height="38" viewBox="0 0 38 38" fill="none" stroke="#fff" stroke-width="2.5">
          <path d="M6 19a13 13 0 0 1 22-9"/><path d="M28 4v7h-7"/>
          <path d="M32 19a13 13 0 0 1-22 9"/><path d="M10 34v-7h7"/>
          <circle cx="19" cy="14" r="2.5" fill="#fff" stroke="none"/>
          <path d="M19 18v8M15 21h8"/>
        </svg>
      </span>
      <p class="feature__text">We will monitor entries closely and promise to provide feedback and guidance on each entry.</p>
    </div>
  </section>

  <footer class="contact-bar">
    <span class="contact-bar__item contact-bar__item--phone">
      <svg width="20" height="22" viewBox="0 0 20 22" fill="none" stroke="#fff" stroke-width="1.8">
        <path d="M5 2l3 5-2 2c1 3 3 6 6 7l2-2 4 3-2 3C9 20 2 12 2 4z"/>
      </svg>
      000000000
    </span>
    <span class="contact-bar__item contact-bar__item--web">
      <svg width="22" height="22" viewBox="0 0 22 22" fill="none" stroke="#fff" stroke-width="1.6">
        <circle cx="11" cy="11" r="9.5"/><ellipse cx="11" cy="11" rx="4.5" ry="9.5"/>
        <path d="M1.5 11h19M3 6h16M3 16h16"/>
      </svg>
      www.ridgeviewlawyers.au
    </span>
  </footer>
</main>
</body>
</html>
```